rt for guide - bartholomew finch personal speaking/consulting website

custom website for my personal speaking/consulting services brand, you can see the basic site we are using as a placeholder at www.rtforguide.example now. I want to re-position this to more of a personal brand site and have video samples of speaking events, downloadable content, a video blog, and links to podcast. I really like the design of dorianwelk.example and the feature set should be fairly similar to his. I'll begin to compile more stock images etc. to use for sliders like he has done, for now we'll need to use stock imagery or existing photography from my social accounts. You can get a feel for social at all platforms/bfinchbroker i.e. facebook.com/bfinchbroker. the site should be primarily geared toward showcasing speaking/consulting services and content, as well as be flexible to allow for additional downloadables etc. in the future.

Target Market(s)

entrepreneurs and leaders looking to grow themselves, their business, and those they lead.

Coding

Coded - Design and coding required

Number of Pages Required

3 page

Font styles to use
Sans Serif

Colors

Designer to choose colors to be used in the design.

Requirements
Must have
• modern slick design, video blog, podcast feed, registration for people to subscribe to newsletter

```html
<!DOCTYPE html>
<html lang="en">
<head>
<meta charset="utf-8">
<title>rt for guide — Bartholomew Finch</title>
<link rel="stylesheet" href="https://fonts.googleapis.com/css2?family=Poppins:wght@400;500;600&display=swap">
<style>
:root{
  --red:#b80000;
  --red-bright:#cc1010;
  --dark:#1f1f1f;
  --ink:#333;
  --muted:#555;
  --grey-band:#efefef;
  --line:#d9d9d9;
  --white:#fff;
}
*{box-sizing:border-box;margin:0;padding:0}
html,body{width:1200px;height:3080px;overflow:hidden}
body{position:relative;font-family:"Poppins",sans-serif;color:var(--ink);background:var(--white)}
.abs{position:absolute}
.btn{position:absolute;background:var(--red);color:var(--white);font-weight:500;display:flex;align-items:center;justify-content:center;border-radius:2px}

/* top bar */
.topbar{left:0;top:0;width:1200px;height:54px;background:var(--red);color:var(--white);font-size:15px}
.topbar .contact{position:absolute;left:136px;top:16px;display:flex;gap:14px;align-items:center}
.topbar .contact span{display:flex;align-items:center;gap:8px}
.topbar nav{position:absolute;right:150px;top:17px;display:flex;gap:28px;font-size:15px}

/* hero */
.hero{left:0;top:54px;width:1200px;height:462px;background:linear-gradient(90deg,#8a8f8a 0%,#6f7a68 30%,#b7b4ad 60%,#d9d6cf 100%)}
.hero-brand{left:136px;top:200px;font-size:40px;font-weight:600;color:#111}
.hero-tag{left:136px;top:300px;font-size:27px;font-weight:600;color:var(--white);line-height:39px}
.arrow{top:274px;width:26px;height:24px;background:#333;display:flex;align-items:center;justify-content:center}

/* subscribe */
.subscribe{left:237px;top:466px;width:729px;height:189px;background:var(--white);border-top:3px solid var(--red);box-shadow:0 6px 18px rgba(0,0,0,.12);text-align:center}
.subscribe p{margin-top:36px;font-size:17.5px;line-height:26px;color:var(--ink)}
.subscribe .email{left:72px;top:104px;width:290px;height:38px;border:1px solid var(--line);font-size:11px;color:#555;padding:10px 9px;text-align:left}
.subscribe .btn{left:371px;top:104px;width:282px;height:36px;font-size:18px;font-weight:400}

/* training */
.section-title{font-size:40px;font-weight:500;color:#333;text-align:center;width:1200px;left:0}
.title-rule{left:567px;top:776px;width:66px;height:1px;background:#777}
.lead{left:160px;top:786px;width:880px;text-align:center;font-size:13px;line-height:24px;color:#222}
.feature{width:270px;text-align:center}
.feature .ring{width:96px;height:96px;margin:0 auto;border:3px solid var(--red);border-radius:50%;background:#fff;display:flex;align-items:center;justify-content:center;box-shadow:0 8px 6px -6px #bbb}
.feature h3{margin-top:22px;font-size:18px;font-weight:500;color:#555}
.feature p{margin-top:12px;font-size:13px;line-height:23px;color:#222}

/* about */
.about-band{left:0;top:1206px;width:1200px;height:475px;background:var(--grey-band)}
.about-photo{left:133px;top:1292px;width:394px;height:303px;background:linear-gradient(90deg,#2a2a2a 0%,#7a2020 35%,var(--red) 60%,var(--red) 100%)}
.about-photo .brand{position:absolute;left:250px;top:90px;font-size:24px;font-weight:600;color:var(--white)}
.about-photo .name{position:absolute;left:236px;top:132px;font-size:14px;color:var(--white)}
.about-text{left:586px;top:1280px;width:470px}
.about-text h2{font-size:33px;font-weight:400;color:#333}
.about-text p{font-size:13px;line-height:23px;color:#444;margin-top:8px}
.ticks{list-style:none;margin-top:10px}
.ticks li{display:flex;gap:12px;align-items:center;font-size:13px;color:#444;height:33px}

/* media */
.media{height:248px;display:flex;align-items:center;justify-content:center}
.media .label{background:rgba(200,40,40,.85);color:var(--white);font-size:17px;font-weight:500;padding:6px 24px}
.media-pod{left:133px;top:1752px;width:437px;background:linear-gradient(90deg,#d8d4c8 0%,#bdb6a2 40%,#3048a8 75%,#2c3f8f 100%)}
.media-speak{left:613px;top:1752px;width:437px;background:linear-gradient(90deg,#b9bab4 0%,#3a3a3a 30%,#8e9a8a 65%,#c6c8c2 100%)}
.download{left:133px;top:2084px;width:460px}
.download h2{font-size:34px;font-weight:400;color:#333}
.download p{font-size:13px;line-height:23px;color:#444;margin-top:6px}
.media-vlog{left:613px;top:2071px;width:437px;height:248px;background:linear-gradient(135deg,#e6e8ea 0%,#cfd3d6 45%,#c02020 70%,#a32424 100%)}

/* inquiry */
.footer{left:0;top:2757px;width:1200px;height:278px;background:var(--dark)}
.inquiry{left:232px;top:2408px;width:706px;height:372px;background:var(--white);border-radius:4px;box-shadow:0 4px 18px rgba(0,0,0,.12)}
.stripe{left:56px;width:593px;height:4px;background:repeating-linear-gradient(90deg,#e36a6a 0 14px,#bbb 14px 16px)}
.inquiry h2{position:absolute;top:28px;width:100%;text-align:center;font-size:33px;font-weight:400;color:#333}
.field{position:absolute;height:42px;border:1px solid #cfcfcf;border-radius:3px;display:flex;align-items:flex-start;font-size:11px;color:#444}
.field .ico{width:36px;height:100%;border-right:1px solid #cfcfcf;display:flex;align-items:center;justify-content:center}
.field span{padding-left:11px;align-self:center}
.field.msg{align-items:flex-start}
.field.msg .ico{height:34px;margin-top:4px}
.field.msg span{align-self:flex-start;margin-top:14px}

/* footer */
.foot-col h4{font-size:16px;font-weight:500;color:var(--white)}
.foot-links{list-style:none;margin-top:14px}
.foot-links li{font-size:13px;color:var(--white);height:27px;display:flex;gap:8px;align-items:center}
.foot-contact .row{display:flex;gap:14px;font-size:13px;color:var(--white);line-height:20px;margin-top:14px}
.foot-brand{left:828px;top:2880px;font-size:44px;font-weight:600;color:var(--white)}
.bottombar{left:0;top:3035px;width:1200px;height:45px;background:var(--red);color:var(--white);font-size:13px}
.bottombar p{position:absolute;left:134px;top:13px}
.social{position:absolute;top:9px;width:27px;height:27px;border:1px solid var(--white)}
</style>
</head>
<body>

<header class="abs topbar">
  <div class="contact">
    <span><svg width="20" height="20" viewBox="0 0 24 24" fill="none" stroke="#fff" stroke-width="1.6"><path d="M5 3h4l2 5-3 2a12 12 0 0 0 6 6l2-3 5 2v4a2 2 0 0 1-2 2A18 18 0 0 1 3 5a2 2 0 0 1 2-2z"/></svg>555 014 2290 2290</span>
    <span>|</span>
    <span><svg width="20" height="20" viewBox="0 0 24 24" fill="none" stroke="#fff" stroke-width="1.6"><rect x="3" y="6" width="18" height="13"/><path d="M3 6l9 7 9-7"/></svg>bfinch@bfinchbroker.example</span>
  </div>
  <nav><span>Home</span><span>Resources</span><span>Contact Us</span></nav>
</header>

<section class="abs hero" role="img" aria-label="Bartholomew Finch in a suit speaking, office plants behind"></section>
<div class="abs hero-brand">rt for guide</div>
<div class="abs hero-tag">The Place Where Entrepreneurs<br>Come To Become Leaders</div>
<div class="abs arrow" style="left:8px"><svg width="10" height="10" viewBox="0 0 10 10"><path d="M7 1L3 5l4 4" stroke="#fff" stroke-width="2" fill="none"/></svg></div>
<div class="abs arrow" style="left:1166px;background:#fff;border:1px solid #333"><svg width="10" height="10" viewBox="0 0 10 10"><path d="M3 1l4 4-4 4" stroke="#333" stroke-width="2" fill="none"/></svg></div>

<section class="abs subscribe">
  <p>Subscribe To This Blog To Get The Latest Tips And Tricks To Help You Be A<br>Successful Enterpreneur</p>
  <div class="abs email">Email address</div>
  <div class="btn">Subscribe to our Podcast</div>
</section>

<h2 class="abs section-title" style="top:714px">Start Your Training Today</h2>
<div class="abs title-rule"></div>
<p class="abs lead">Lorem ipsum dolor sit amet, consectetuer adipiscing elit, sed diam nonummy nibh euismod tincidunt ut laoreet dolore magna aliquam erat volutpat. Ut wisi enim ad minim veniam.</p>

<div class="abs feature" style="left:141px;top:848px">
  <div class="ring"><svg width="52" height="40" viewBox="0 0 52 40" fill="#222"><circle cx="9" cy="14" r="4"/><rect x="5" y="19" width="8" height="16" rx="2"/><circle cx="20" cy="12" r="4"/><rect x="16" y="17" width="8" height="18" rx="2"/><circle cx="32" cy="12" r="4"/><rect x="28" y="17" width="8" height="18" rx="2"/><circle cx="43" cy="14" r="4"/><rect x="39" y="19" width="8" height="16" rx="2"/></svg></div>
  <h3>Leadership Skills</h3>
  <p>Lorem ipsum dolor sit amet, consuer adipiscing elit, sed diam nonummy nibh euismod tincidunt ut.</p>
</div>
<div class="abs feature" style="left:460px;top:848px">
  <div class="ring"><svg width="44" height="44" viewBox="0 0 44 44" fill="none" stroke="#222" stroke-width="3"><circle cx="22" cy="19" r="8"/><path d="M18 30h8M19 35h6M22 3v5M8 19H3M41 19h-5M11 8l3 3M33 8l-3 3"/></svg></div>
  <h3>Entrepreneurs</h3>
  <p>Lorem ipsum dolor sit amet, consuer adipiscing elit, sed diam nonummy nibh euismod tincidunt ut.</p>
</div>
<div class="abs feature" style="left:778px;top:848px">
  <div class="ring"><svg width="48" height="48" viewBox="0 0 48 48" fill="#222"><circle cx="24" cy="8" r="4"/><rect x="20" y="13" width="8" height="10" rx="2"/><circle cx="13" cy="22" r="4"/><rect x="9" y="27" width="8" height="14" rx="2"/><circle cx="35" cy="22" r="4"/><rect x="31" y="27" width="8" height="14" rx="2"/><rect x="19" y="26" width="10" height="15" rx="2"/></svg></div>
  <h3>Team Building</h3>
  <p>Lorem ipsum dolor sit amet, consuer adipiscing elit, sed diam nonummy nibh euismod tincidunt ut.</p>
</div>
<div class="btn" style="left:526px;top:1102px;width:147px;height:34px;font-size:16px">Get Started</div>

<section class="abs about-band"></section>
<div class="abs about-photo" role="img" aria-label="Portrait of Bartholomew Finch in a suit on a red background">
  <span class="brand">rt for guide</span>
  <span class="name">Bartholomew Finch</span>
</div>
<div class="abs about-text">
  <h2>About Me</h2>
  <p>Dlore magna aliquam erat volutpat. Ut wisi enim ad minim veniam, quis nostrud exerci.</p>
  <p style="margin-top:4px">Lorem ipsum dolor sit amet, consectetuer adipiscing elit, sed donummy nibh euismod tincidunt ut laoreet dolore magna aliquam erat volutpat. Ut wisi enim ad minim veniam, quis nostrud exerci.</p>
  <ul class="ticks">
    <li><svg width="14" height="14" viewBox="0 0 14 14" fill="none" stroke="#b80000" stroke-width="1.6"><circle cx="7" cy="7" r="5.5"/><path d="M4 7l2 2 6-6"/></svg>Duis autem vel eum iriure dolor in hendrerit in vulputate.</li>
    <li><svg width="14" height="14" viewBox="0 0 14 14" fill="none" stroke="#b80000" stroke-width="1.6"><circle cx="7" cy="7" r="5.5"/><path d="M4 7l2 2 6-6"/></svg>Velit esse olestie consequat, vel illum dolore eu feugiat.</li>
    <li><svg width="14" height="14" viewBox="0 0 14 14" fill="none" stroke="#b80000" stroke-width="1.6"><circle cx="7" cy="7" r="5.5"/><path d="M4 7l2 2 6-6"/></svg>Nulla facilisis at vero erocumsan et iusto odio dignissim qui.</li>
  </ul>
</div>
<div class="btn" style="left:587px;top:1564px;width:147px;height:35px;font-size:14px">Contact Us Today</div>

<div class="abs media media-pod" role="img" aria-label="Video still of Bartholomew Finch recording a podcast"><span class="label">Podcasts</span></div>
<div class="abs media media-speak" role="img" aria-label="Video still of Bartholomew Finch at a speaking event"><span class="label">Speaking Events</span></div>

<div class="abs download">
  <h2>Downloadable Content</h2>
  <p>Dlore magna aliquam erat volutpat. Ut wisi enim ad minim veniam, quis nostrud exerci.</p>
  <p>Ready for more?&nbsp; Lorem ipsum dolor sit amet, consectetuer adipiscing elit, sed diam nonummy nibh euismod tincidunt ut laoreet dolore magna aliquam erat volutpat.</p>
</div>
<div class="btn" style="left:133px;top:2261px;width:204px;height:35px;font-size:14px">Visit Our Resources Page</div>
<div class="abs media-vlog" role="img" aria-label="Video blog still of Bartholomew Finch talking to camera in an office"></div>

<footer class="abs footer"></footer>

<section class="abs inquiry">
  <div class="abs stripe" style="top:-2px"></div>
  <h2>Quick Inquiry</h2>
  <div class="field" style="left:56px;top:87px;width:289px"><div class="ico"><svg width="12" height="12" viewBox="0 0 12 12" fill="#b80000"><circle cx="6" cy="3.5" r="3"/><path d="M0 12a6 5 0 0 1 12 0z"/></svg></div><span>First Name*</span></div>
  <div class="field" style="left:361px;top:87px;width:289px"><div class="ico"><svg width="12" height="12" viewBox="0 0 12 12" fill="#b80000"><circle cx="6" cy="3.5" r="3"/><path d="M0 12a6 5 0 0 1 12 0z"/></svg></div><span>Last Name*</span></div>
  <div class="field" style="left:56px;top:142px;width:289px"><div class="ico"><svg width="12" height="12" viewBox="0 0 24 24" fill="#b80000"><path d="M5 3h4l2 5-3 2a12 12 0 0 0 6 6l2-3 5 2v4a2 2 0 0 1-2 2A18 18 0 0 1 3 5a2 2 0 0 1 2-2z"/></svg></div><span>Your Phone*</span></div>
  <div class="field" style="left:361px;top:142px;width:289px"><div class="ico"><svg width="12" height="10" viewBox="0 0 12 10" fill="#b80000"><path d="M0 0h12v1L6 5 0 1z M0 3l6 4 6-4v7H0z"/></svg></div><span>Your Email*</span></div>
  <div class="field msg" style="left:56px;top:197px;width:594px;height:84px"><div class="ico"><svg width="13" height="11" viewBox="0 0 13 11" fill="#b80000"><ellipse cx="5" cy="4" rx="5" ry="3.5"/><ellipse cx="8.5" cy="7" rx="4.5" ry="3"/></svg></div><span>Your Message*</span></div>
  <div class="btn" style="left:322px;top:299px;width:91px;height:35px;font-size:18px">Submit</div>
  <div class="abs stripe" style="bottom:-2px"></div>
</section>

<div class="abs foot-col" style="left:133px;top:2826px">
  <h4>Quick Links</h4>
  <ul class="foot-links">
    <li>›&nbsp;Home</li><li>›&nbsp;About Me</li><li>›&nbsp;Services</li><li>›&nbsp;Resources</li><li>›&nbsp;Contact Us</li>
  </ul>
</div>
<div class="abs foot-col foot-contact" style="left:416px;top:2826px">
  <h4>Contact Details</h4>
  <div class="row"><svg width="12" height="16" viewBox="0 0 12 16" fill="#b80000"><path d="M6 0a6 6 0 0 1 6 6c0 4-6 10-6 10S0 10 0 6a6 6 0 0 1 6-6z"/><circle cx="6" cy="6" r="2" fill="#1f1f1f"/></svg><span>Street Name, City Name, State<br>Zipcode</span></div>
  <div class="row" style="margin-top:18px"><svg width="16" height="16" viewBox="0 0 24 24" fill="none" stroke="#b80000" stroke-width="1.6"><rect x="3" y="6" width="18" height="13"/><path d="M3 6l9 7 9-7"/></svg><span>bfinch@bfinchbroker.example</span></div>
  <div class="row" style="margin-top:18px"><svg width="16" height="16" viewBox="0 0 24 24" fill="none" stroke="#b80000" stroke-width="1.6"><path d="M5 3h4l2 5-3 2a12 12 0 0 0 6 6l2-3 5 2v4a2 2 0 0 1-2 2A18 18 0 0 1 3 5a2 2 0 0 1 2-2z"/></svg><span>555 014 2290 2290</span></div>
</div>
<div class="abs foot-brand">rt for guide</div>

<div class="abs bottombar">
  <p>Copyright © 2019 &nbsp;Brightline Studio. &nbsp;All Right Reserved</p>
  <span class="social" style="left:952px"></span>
  <span class="social" style="left:988px"></span>
  <span class="social" style="left:1024px"></span>
</div>

</body>
</html>
```